Australian Solar Smart Home Provider needs business card design

We need a simple, clean, business card that shows who we are and gives the brand feeling. Please see the website (www.plovenix.com) and the attached logo as well. Please use this logo on the business card. As a business we do residential solar, batteries, smart home technology, and hot water solutions. We want the feeling to be accessible to ages 40-65 but at the same time be a bit on the technologically savvy side.
Also the primary purpose of the business card is to hand of and drive referrals - so we want everyone to have a referral code on the card and that aspect should stand out.
Things we want on the card with an example employee:
Name: Marcus Pellwood
Position: Director of Sales and Marketing
telephone number office: 02 8765 4312
telephone number mobile: 0428 915 603
address: Suite 402, 18 Brindle Lane, Sydney, NSW 2000
website: www.plovenix.com
Target Market(s)
Homeowners aged 35-60
Industry/Entity Type
Residential
Contact Information for Business Card
Name: Marcus Pellwood
website: www.plovenix.com
referral code: Mpellwood
Look and feel

```html
<!DOCTYPE html>
<html lang="en">
<head>
<meta charset="UTF-8">
<title>Plovenix Business Card</title>
<link href="https://fonts.googleapis.com/css2?family=Open+Sans:wght@300;400;600;700&display=swap" rel="stylesheet">
<style>
  :root {
    --backdrop: #efefef;
    --card: #ffffff;
    --lime: #a6c92e;
    --leaf: #3b9a37;
    --stone: #9c9c9c;
    --mist: #b4b4b4;
    --band-text: #ffffff;
  }
  * { margin: 0; padding: 0; box-sizing: border-box; }
  html, body {
    width: 1200px;
    height: 1000px;
    overflow: hidden;
    background: var(--backdrop);
    font-family: "Open Sans", Arial, sans-serif;
  }
  .stage {
    width: 1200px;
    height: 1000px;
    display: flex;
    align-items: center;
    justify-content: center;
  }
  .business-card {
    position: relative;
    width: 900px;
    height: 550px;
    background: var(--card);
    box-shadow: 0 6px 18px rgba(0, 0, 0, 0.08);
    overflow: hidden;
  }
  .brand {
    position: absolute;
    left: 110px;
    top: 175px;
    display: flex;
    align-items: center;
    gap: 16px;
  }
  .brand-dot {
    width: 56px;
    height: 56px;
    border-radius: 50%;
    background: var(--lime);
  }
  .brand-name {
    font-size: 62px;
    font-weight: 600;
    color: var(--stone);
    letter-spacing: -1px;
    line-height: 1;
  }
  .contact-block {
    position: absolute;
    left: 468px;
    top: 258px;
  }
  .person-name {
    font-size: 31px;
    font-weight: 300;
    color: var(--stone);
    text-transform: uppercase;
    line-height: 1.1;
  }
  .person-role {
    font-size: 23px;
    font-weight: 700;
    color: var(--leaf);
    margin-top: 2px;
  }
  .details {
    list-style: none;
    margin-top: 20px;
  }
  .detail {
    display: flex;
    align-items: flex-start;
    gap: 14px;
    font-size: 20px;
    font-weight: 300;
    color: var(--mist);
    line-height: 1.3;
    margin-bottom: 2px;
  }
  .detail-icon {
    width: 20px;
    height: 24px;
    flex: none;
    margin-top: 1px;
    fill: var(--lime);
  }
  .footer-band {
    position: absolute;
    left: 0;
    right: 0;
    bottom: 0;
    height: 66px;
    background: var(--lime);
    display: flex;
    align-items: center;
    justify-content: space-between;
    padding: 0 70px 0 110px;
    color: var(--band-text);
    font-size: 19px;
    font-weight: 400;
  }
</style>
</head>
<body>
<main class="stage">
  <article class="business-card">
    <div class="brand">
      <span class="brand-dot"></span>
      <span class="brand-name">plovenix</span>
    </div>

    <section class="contact-block">
      <h1 class="person-name">Marcus Pellwood</h1>
      <p class="person-role">Director of Sales and Marketing</p>
      <ul class="details">
        <li class="detail">
          <svg class="detail-icon" viewBox="0 0 20 24" aria-hidden="true">
            <path d="M10 0C4.8 0 1 3.9 1 8.8 1 15 10 24 10 24s9-9 9-15.2C19 3.9 15.2 0 10 0zm0 12.2a3.5 3.5 0 1 1 0-7 3.5 3.5 0 0 1 0 7z"/>
          </svg>
          <span>Suite 402, 18 Brindle Lane,<br>Sydney, NSW 2000</span>
        </li>
        <li class="detail">
          <svg class="detail-icon" viewBox="0 0 20 24" aria-hidden="true">
            <path d="M4.5 1.5l3 4.5-2 2.2c1.2 3.3 3.4 5.9 6.4 7.6l2.1-2 4.4 3.1-2.2 4.1C8.5 20.5 2.3 12.4 1.2 3.7z"/>
          </svg>
          <span>02 8765 4312</span>
        </li>
        <li class="detail">
          <svg class="detail-icon" viewBox="0 0 20 24" aria-hidden="true">
            <path d="M4 0h12a2 2 0 0 1 2 2v20a2 2 0 0 1-2 2H4a2 2 0 0 1-2-2V2a2 2 0 0 1 2-2zm0 3v15h12V3zm6 16.5a1.3 1.3 0 1 0 0 2.6 1.3 1.3 0 0 0 0-2.6z"/>
          </svg>
          <span>0428 915 603</span>
        </li>
      </ul>
    </section>

    <footer class="footer-band">
      <span class="website">www.plovenix.com</span>
      <span class="referral">Referral code: Mpellwood</span>
    </footer>
  </article>
</main>
</body>
</html>
```